BRISKET Homes business card Pelmo Press

I've been a Real Estate agent since 1988. I left the BIG brokerages 2 years ago and am on my own and need a business card. I love doing graphics, but don't have the bandwidth right now.

Background. I want a card that stands out like I do. I'm the fun guy that always has a joke or funny story, and my clients like me. Something fun, but not too silly.

I don't have a symbol or logo that I'm using on the card now, but need to include something, a Font by itself or a logo? I'm not sure if we need a logo or not. I'm open.
The GREAT design is going to be the basis for the next project of stationary, note pads, and Real Estate FOR SALE & Open House signs.

Single sided card is fine, but I selected a 2 sided just in case that's what it works out to be.

Here we go. If you need anything else. Please let me know. As I think of anything, I'll add that also.

Target Market(s)

My territory is Santa Clara County / Silicon Valley, CA. I tend to work with new buyers buying a condo ($500,000) up to single family home for about $1.5 million. 1st time buyers and also move-up buyers. I haven't worked with multi-million $$ homes .... but wouldn't turn it down. Clients here tend to be White, Latin and now many more Chinese and East Indians. Clients also tend to be high tech, Zorvat, Quince, Lumigrid workers and also non tech people.

Industry/Entity Type

Business

Contact Information for Business Card

CONTENT:
Company: BRISKET Homes
My name: Harold P. Brisket Jr.
Title: Real Estate Broker
Email: Hal@HaroldBrisket.example
Website: www.HaroldBrisket.example
Phone: (408) 555-0173
BRE # 07395162

Font styles to use
Sans Serif

Requirements
Must have
• Content from above. Something that stands out from the others. Serious enough looking, not stale, maybe a bit fun.

```html
<!DOCTYPE html>
<html lang="en">
<head>
<meta charset="utf-8">
<title>BRISKET Homes – Business Card</title>
<link rel="stylesheet" href="https://fonts.googleapis.com/css2?family=Courgette&family=Open+Sans:wght@400;600;700;800&display=swap">
<style>
  :root {
    --page: #e6e3de;
    --card: #f4f1ea;
    --red: #9b1c24;
    --green: #7cbf3a;
    --orange: #f4b133;
    --brown: #a5632a;
    --ink: #2e2e2e;
  }
  * { box-sizing: border-box; margin: 0; padding: 0; }
  html, body { width: 1200px; height: 968px; overflow: hidden; }
  body {
    background: var(--page);
    font-family: "Open Sans", Arial, sans-serif;
    color: var(--ink);
    display: flex;
    flex-direction: column;
    align-items: center;
    justify-content: center;
    gap: 64px;
  }
  .card {
    position: relative;
    width: 700px;
    height: 400px;
    background: var(--card);
    border-radius: 4px;
    box-shadow: 0 6px 18px rgba(0,0,0,.18);
    overflow: hidden;
  }
  .card-band {
    position: absolute;
    left: 0; right: 0; bottom: 0;
    height: 48px;
    background: linear-gradient(90deg, var(--green) 0%, var(--red) 45%, var(--red) 70%, var(--orange) 100%);
    opacity: .9;
  }

  /* Logo side */
  .brand-lockup {
    position: absolute;
    top: 92px; left: 0; right: 0;
    display: flex; flex-direction: column; align-items: center;
  }
  .brand-mark {
    width: 96px; height: 96px; border-radius: 50%;
    background: var(--green);
    margin-bottom: 18px;
  }
  .brand-name {
    font-weight: 800; font-size: 46px; letter-spacing: 1px;
    color: var(--red); line-height: 1;
  }
  .brand-web {
    margin-top: 12px;
    font-weight: 700; font-size: 17px; letter-spacing: .5px;
    color: var(--brown);
  }

  /* Contact side */
  .person { position: absolute; top: 88px; left: 48px; }
  .person-name {
    font-family: "Courgette", cursive;
    font-weight: 400;
    font-size: 34px; color: var(--ink);
  }
  .person-title { margin-top: 4px; font-size: 16px; color: var(--red); font-weight: 600; }

  .mini-brand {
    position: absolute; top: 52px; right: 44px;
    display: flex; align-items: center; gap: 8px;
  }
  .mini-brand .brand-mark { width: 24px; height: 24px; margin: 0; }
  .mini-brand .brand-name { font-size: 22px; letter-spacing: .5px; }

  .contact-list {
    position: absolute; top: 158px; right: 44px;
    list-style: none;
    display: flex; flex-direction: column; gap: 12px;
    font-size: 15px; font-weight: 600;
  }
  .contact-item { display: flex; align-items: center; gap: 10px; }
  .contact-icon { width: 24px; height: 24px; flex: none; }
</style>
</head>
<body>

<section class="card card-back" aria-label="Card back">
  <div class="brand-lockup">
    <span class="brand-mark"></span>
    <span class="brand-name">BRISKET HOMES</span>
    <span class="brand-web">www.HaroldBrisket.example</span>
  </div>
  <div class="card-band" role="img" aria-label="Decorative colour band in green, red and orange"></div>
</section>

<section class="card card-front" aria-label="Card front">
  <div class="mini-brand">
    <span class="brand-mark"></span>
    <span class="brand-name">BRISKET HOMES</span>
  </div>
  <div class="person">
    <h1 class="person-name">Harold P. Brisket Jr.</h1>
    <p class="person-title">Real Estate Broker</p>
  </div>
  <ul class="contact-list">
    <li class="contact-item">
      <svg class="contact-icon" viewBox="0 0 24 24" aria-hidden="true">
        <circle cx="12" cy="12" r="12" fill="var(--orange)"/>
        <rect x="6" y="8" width="12" height="8" rx="1" fill="none" stroke="#fff" stroke-width="1.6"/>
        <path d="M6.5 8.5 L12 13 L17.5 8.5" fill="none" stroke="#fff" stroke-width="1.6"/>
      </svg>
      <span>Hal@HaroldBrisket.example</span>
    </li>
    <li class="contact-item">
      <svg class="contact-icon" viewBox="0 0 24 24" aria-hidden="true">
        <circle cx="12" cy="12" r="12" fill="var(--red)"/>
        <path fill="#fff" d="M8.2 6.5 L10 6.2 L11 9 L9.8 10.2 C10.4 11.7 12.3 13.6 13.8 14.2 L15 13 L17.8 14 L17.5 15.8 C17.3 16.8 16.3 17.6 15 17.4 C10.8 16.7 7.3 13.2 6.6 9 C6.4 7.7 7.2 6.7 8.2 6.5 Z"/>
      </svg>
      <span>(408) 555-0173 &nbsp;BRE # 07395162</span>
    </li>
  </ul>
  <div class="card-band" role="img" aria-label="Decorative colour band in green, red and orange"></div>
</section>

</body>
</html>
```